Restaurant Menu for beach club in Martinique

We would like to set a new design for our Menu. We are a restaurant, and beach club, located in Martinique. Our website is available at : http://www.korivagueplage.net Regards

Colors

Designer to choose colors to be used in the design.

```html
<!DOCTYPE html>
<html lang="fr">
<head>
<meta charset="utf-8">
<title>Kori Vague — Les Entrées</title>
<link href="https://fonts.googleapis.com/css2?family=Montserrat:wght@600;700&family=Yellowtail&family=Libre+Baskerville&display=swap" rel="stylesheet">
<style>
  :root {
    --page-bg: #e6e6e6;
    --board: #3b3b3b;
    --board-light: #474747;
    --gold: #f6a927;
    --chalk: #ffffff;
    --note: #e4e4e4;
    --rule: #8a8a8a;
  }
  * { box-sizing: border-box; margin: 0; padding: 0; }
  html, body { width: 1200px; height: 1200px; overflow: hidden; background: var(--page-bg); }
  .menu {
    position: absolute; left: 185px; top: 15px; width: 830px; height: 1170px;
    background: linear-gradient(125deg, var(--board-light) 0%, var(--board-light) 38%, var(--board) 38.2%, var(--board) 100%);
    overflow: hidden;
  }
  .shore { position: absolute; left: 0; bottom: 0; width: 830px; height: 185px; }
  .brand {
    position: absolute; top: 48px; left: 0; width: 100%;
    display: flex; justify-content: center; align-items: center; gap: 14px;
    font-family: "Montserrat", sans-serif; font-weight: 600; font-size: 38px;
    letter-spacing: 6px; color: var(--chalk);
  }
  .brand-dot { width: 14px; height: 14px; border-radius: 50%; background: var(--chalk); }
  .column-divider { position: absolute; left: 415px; top: 159px; width: 2px; height: 827px; background: var(--rule); }
  .section-rule { position: absolute; height: 2px; background: var(--rule); }
  .section-title {
    position: absolute; width: 360px; display: flex; justify-content: center; align-items: center; gap: 18px;
    font-family: "Yellowtail", cursive; font-weight: 400; font-size: 36px; line-height: 1.2; color: var(--chalk);
  }
  .section-title::before, .section-title::after { content: ""; width: 38px; height: 4px; background: var(--chalk); }
  .dish { position: absolute; width: 340px; text-align: center; }
  .dish-line {
    display: flex; align-items: flex-end; justify-content: center;
    font-family: "Montserrat", sans-serif; font-weight: 700; color: var(--gold);
  }
  .dish-name { font-size: 15px; line-height: 1; text-align: right; white-space: nowrap; flex: none; }
  .dish-leader { flex: 0 1 120px; min-width: 16px; border-bottom: 2px dotted var(--gold); margin: 0 1px 3px; }
  .dish-price { font-size: 21px; line-height: 1; white-space: nowrap; flex: none; }
  .dish-note {
    margin-top: 3px; font-family: "Libre Baskerville", serif; font-size: 9.5px; line-height: 14px; color: var(--note);
    white-space: nowrap;
  }
  .col-left { left: 41px; }
  .col-right { left: 428px; }
</style>
</head>
<body>
<main class="menu">
  <svg class="shore" viewBox="0 0 830 185">
    <defs>
      <linearGradient id="terrace" x1="0" y1="0" x2="1" y2="0">
        <stop offset="0" stop-color="#8fb7bd"/>
        <stop offset="0.45" stop-color="#c98a6a"/>
        <stop offset="0.75" stop-color="#b2c9c8"/>
        <stop offset="1" stop-color="#6d5a4c"/>
      </linearGradient>
    </defs>
    <path role="img" aria-label="Photo de cocktails sur une table de terrasse face à la mer" d="M0 44 C120 60 260 82 420 66 C560 50 700 30 830 40 V185 H0 Z" fill="url(#terrace)"/>
    <path d="M0 38 C120 52 260 74 420 58 C560 40 700 18 830 26 V40 C700 30 560 50 420 66 C260 82 120 60 0 44 Z" fill="var(--gold)"/>
  </svg>

  <header class="brand"><span class="brand-dot"></span>KORI VAGUE</header>

  <div class="column-divider"></div>

  <h2 class="section-title" style="left:31px; top:150px;">Les Entrées</h2>
  <h2 class="section-title" style="left:418px; top:150px;">Nos Entrées</h2>

  <section class="entrees-list">
    <div class="dish col-left" style="top:217px"><div class="dish-line"><span class="dish-name">L’ assiette «zen»</span><span class="dish-leader"></span><span class="dish-price">9,80 €</span></div><p class="dish-note">(nem de gambas, maki au saumon, mini brochette de poulet,<br>samoussa au chèvre frais)</p></div>
    <div class="dish col-left" style="top:286px"><div class="dish-line"><span class="dish-name">Les nems aux deux saumons</span><span class="dish-leader"></span><span class="dish-price">9,50 €</span></div><p class="dish-note">sauce crémeuse au wasabi et salade de pousses d’épinards</p></div>
    <div class="dish col-left" style="top:342px"><div class="dish-line"><span class="dish-name">La salade du « Périgord »</span><span class="dish-leader"></span><span class="dish-price">13,10 €</span></div><p class="dish-note">(Salade, roquette, oignons rouges, foie gras maison, gésiers confits,<br>magrets fumés et pommes)</p></div>
    <div class="dish col-left" style="top:411px"><div class="dish-line"><span class="dish-name">Le tartare de loup à la<br>moutarde de Reims</span><span class="dish-leader"></span><span class="dish-price">10,50 €</span></div><p class="dish-note">sur une gelée de concombres</p></div>
    <div class="dish col-left" style="top:480px"><div class="dish-line"><span class="dish-name">Le bavarois de tomates</span><span class="dish-leader"></span><span class="dish-price">8,20 €</span></div><p class="dish-note">farci au chèvre frais et jus de betteraves</p></div>
    <div class="dish col-left" style="top:536px"><div class="dish-line"><span class="dish-name">Le royal de foie gras</span><span class="dish-leader"></span><span class="dish-price">10,50 €</span></div><p class="dish-note">et rouleau de printemps au poulet et vermicelles</p></div>
    <div class="dish col-left" style="top:591px"><div class="dish-line"><span class="dish-name">Le tartare de St Jacques</span><span class="dish-leader"></span><span class="dish-price">12,50 €</span></div><p class="dish-note">aux échalotes rôties et concombres</p></div>
    <div class="dish col-left" style="top:647px"><div class="dish-line"><span class="dish-name">L’oeuf “cocotte”</span><span class="dish-leader"></span><span class="dish-price">9,50 €</span></div><p class="dish-note">à la crème de morilles et jambon ibérique</p></div>
    <div class="dish col-left" style="top:702px"><div class="dish-line"><span class="dish-name">La salade de légumes</span><span class="dish-leader"></span><span class="dish-price">9,80 €</span></div><p class="dish-note">croquants et gambas façon thaï</p></div>
    <div class="dish col-left" style="top:758px"><div class="dish-line"><span class="dish-name">Le foie gras de canard</span><span class="dish-leader"></span><span class="dish-price">13,80 €</span></div><p class="dish-note">au vieux porto, brioche maison</p></div>
    <div class="dish col-left" style="top:813px"><div class="dish-line"><span class="dish-name">Le gâteau de lapereau</span><span class="dish-leader"></span><span class="dish-price">9,80 €</span></div><p class="dish-note">au lard paysan, farci au foie gras, compote d’oignons rouges</p></div>
    <div class="dish col-left" style="top:869px"><div class="dish-line"><span class="dish-name">La verrine aux 3 choux-fleurs</span><span class="dish-leader"></span><span class="dish-price">11,50 €</span></div><p class="dish-note">crabe et saumon fumé</p></div>
    <div class="dish col-left" style="top:924px"><div class="dish-line"><span class="dish-name">Le foie gras frais</span><span class="dish-leader" style="flex-basis:40px"></span><span class="dish-price">12,50 €</span></div><p class="dish-note">poêlé aux cèpes et son jus corsé de canard</p></div>
  </section>

  <section class="entrees-list">
    <div class="dish col-right" style="top:217px"><div class="dish-line"><span class="dish-name">L’ assiette «zen»</span><span class="dish-leader"></span><span class="dish-price">9,80 €</span></div><p class="dish-note">(nem de gambas, maki au saumon, mini brochette de poulet,<br>samoussa au chèvre frais)</p></div>
    <div class="dish col-right" style="top:286px"><div class="dish-line"><span class="dish-name">Les nems aux deux saumons</span><span class="dish-leader"></span><span class="dish-price">9,50 €</span></div><p class="dish-note">sauce crémeuse au wasabi et salade de pousses d’épinards</p></div>
    <div class="dish col-right" style="top:342px"><div class="dish-line"><span class="dish-name">La salade du « Périgord »</span><span class="dish-leader"></span><span class="dish-price">13,10 €</span></div><p class="dish-note">(Salade, roquette, oignons rouges, foie gras maison, gésiers confits,<br>magrets fumés et pommes)</p></div>
    <div class="dish col-right" style="top:411px"><div class="dish-line"><span class="dish-name">Le tartare de loup à la<br>moutarde de Reims</span><span class="dish-leader"></span><span class="dish-price">10,50 €</span></div><p class="dish-note">sur une gelée de concombres</p></div>
    <div class="dish col-right" style="top:480px"><div class="dish-line"><span class="dish-name">Le bavarois de tomates</span><span class="dish-leader"></span><span class="dish-price">8,20 €</span></div><p class="dish-note">farci au chèvre frais et jus de betteraves</p></div>
    <div class="dish col-right" style="top:536px"><div class="dish-line"><span class="dish-name">Le royal de foie gras</span><span class="dish-leader"></span><span class="dish-price">10,50 €</span></div><p class="dish-note">et rouleau de printemps au poulet et vermicelles</p></div>
  </section>

  <div class="section-rule" style="left:441px; top:592px; width:352px;"></div>
  <h2 class="section-title" style="left:418px; top:602px;">Nos Entrées</h2>

  <section class="entrees-list">
    <div class="dish col-right" style="top:668px"><div class="dish-line"><span class="dish-name">L’ assiette «zen»</span><span class="dish-leader"></span><span class="dish-price">9,80 €</span></div><p class="dish-note">(nem de gambas, maki au saumon, mini brochette de poulet,<br>samoussa au chèvre frais)</p></div>
    <div class="dish col-right" style="top:738px"><div class="dish-line"><span class="dish-name">Les nems aux deux saumons</span><span class="dish-leader"></span><span class="dish-price">9,50 €</span></div><p class="dish-note">sauce crémeuse au wasabi et salade de pousses d’épinards</p></div>
    <div class="dish col-right" style="top:793px"><div class="dish-line"><span class="dish-name">La salade du « Périgord »</span><span class="dish-leader"></span><span class="dish-price">13,10 €</span></div><p class="dish-note">(Salade, roquette, oignons rouges, foie gras maison, gésiers confits,<br>magrets fumés et pommes)</p></div>
    <div class="dish col-right" style="top:863px"><div class="dish-line"><span class="dish-name">Le tartare de loup à la<br>moutarde de Reims</span><span class="dish-leader"></span><span class="dish-price">10,50 €</span></div><p class="dish-note">sur une gelée de concombres</p></div>
    <div class="dish col-right" style="top:932px"><div class="dish-line"><span class="dish-name">Le bavarois de tomates</span><span class="dish-leader"></span><span class="dish-price">8,20 €</span></div><p class="dish-note">farci au chèvre frais et jus de betteraves</p></div>
  </section>

  <div class="section-rule" style="left:31px; top:986px; width:352px;"></div>
  <div class="section-rule" style="left:441px; top:986px; width:352px;"></div>
</main>
</body>
</html>
```